Criação de Cartao de Visita para Computador & Internet
" Nossos clientes fazem o outsorcing da TI para nós, assim cuidamos de todos os recursos se serviços de TI, também vendemos hardwares e softwares "

```html
<!DOCTYPE html>
<html lang="pt-BR">
<head>
<meta charset="utf-8">
<title>Cartão de Visita – Vértice TI</title>
<link rel="stylesheet" href="https://fonts.googleapis.com/css2?family=Open+Sans:wght@400;600;700&display=swap">
<style>
  :root {
    --blue: #1a82c4;
    --blue-dark: #0f5f97;
    --blue-light: #3fa3dd;
    --ink: #4a4f55;
    --ink-soft: #6d737a;
    --paper: #ffffff;
    --paper-shade: #eef1f4;
    --canvas: #3a3d42;
  }
  * { box-sizing: border-box; margin: 0; padding: 0; }
  html, body { width: 1200px; height: 1200px; overflow: hidden; }
  body {
    background: var(--canvas);
    font-family: "Open Sans", Arial, sans-serif;
    color: var(--ink);
    display: flex;
    flex-direction: column;
    align-items: center;
    justify-content: center;
    gap: 44px;
  }
  .card {
    position: relative;
    width: 900px;
    height: 514px;
    border-radius: 26px;
    overflow: hidden;
    background: var(--paper);
  }

  /* Front */
  .card-front {
    background: linear-gradient(180deg, var(--paper) 0%, var(--paper-shade) 100%);
  }
  .front-band {
    position: absolute; left: 0; right: 0; bottom: 0; height: 62px;
    background: linear-gradient(90deg, var(--blue-dark), var(--blue-light));
  }
  .brand {
    position: absolute; left: 70px; top: 0; bottom: 62px;
    display: flex; align-items: center; gap: 14px;
  }
  .brand-dot {
    width: 26px; height: 26px; border-radius: 50%;
    background: var(--blue);
  }
  .brand-name {
    color: var(--blue); font-weight: 700; font-size: 46px; line-height: 1;
  }
  .identity { position: absolute; left: 420px; top: 110px; }
  .person-name { font-size: 38px; font-weight: 400; color: var(--ink); }
  .person-role { font-size: 20px; font-weight: 600; color: var(--ink-soft); margin-top: 2px; }
  .division { font-size: 18px; font-weight: 700; color: var(--blue); margin-top: 6px; letter-spacing: 0.5px; }
  .contacts { list-style: none; margin-top: 18px; }
  .contacts li {
    display: flex; align-items: center; gap: 10px;
    font-size: 15px; color: var(--ink-soft); line-height: 1.55;
  }
  .contacts .icon { width: 20px; height: 20px; flex: none; }
  .contacts .phones { display: flex; flex-direction: column; }

  /* Back */
  .back-top {
    position: absolute; left: 0; right: 0; top: 0; height: 250px;
    background: linear-gradient(90deg, var(--blue-dark), var(--blue-light));
    color: var(--paper);
  }
  .section-head { text-align: center; font-weight: 700; line-height: 1.25; }
  .section-head .kicker { font-size: 20px; }
  .section-head .title { font-size: 24px; }
  .back-top .section-head { padding-top: 36px; }
  .service-list {
    list-style: none;
    display: grid;
    grid-template-columns: 1fr 1fr;
    column-gap: 40px; row-gap: 8px;
    padding: 24px 80px 0;
    font-size: 16px;
  }
  .service-list li::before { content: "• "; }
  .back-bottom { position: absolute; left: 0; right: 0; top: 250px; bottom: 0; color: var(--blue-dark); }
  .back-bottom .section-head { padding-top: 34px; }
  .event-list {
    list-style: none;
    display: grid;
    grid-template-columns: repeat(3, 1fr);
    row-gap: 8px;
    padding: 22px 110px 0;
    font-size: 16px;
    color: var(--blue);
  }
  .event-list li::before { content: "• "; }
  .back-edge {
    position: absolute; left: 0; right: 0; bottom: 0; height: 16px;
    background: var(--blue);
  }
</style>
</head>
<body>

  <section class="card card-front">
    <div class="front-band"></div>
    <div class="brand"><span class="brand-dot"></span><span class="brand-name">Vértice TI</span></div>
    <div class="identity">
      <h1 class="person-name">Marina Castelo</h1>
      <p class="person-role">Diretora Executiva</p>
      <p class="division">DIVISÃO DE EVENTOS</p>
      <ul class="contacts">
        <li>
          <svg class="icon" viewBox="0 0 20 20"><circle cx="10" cy="10" r="9" fill="none" stroke="#6d737a" stroke-width="1.5"/><path d="M7 5.5l2 2-1 1.2a6 6 0 0 0 3.3 3.3l1.2-1 2 2-1.3 1.5C9.5 14 6 10.5 5.5 6.8z" fill="#6d737a"/></svg>
          <span class="phones"><span>11 4002-1190 (São Paulo)</span><span>0800 700 3150 (Demais localidades)</span></span>
        </li>
        <li>
          <svg class="icon" viewBox="0 0 20 20"><circle cx="10" cy="10" r="9" fill="none" stroke="#6d737a" stroke-width="1.5"/><rect x="7" y="4.5" width="6" height="11" rx="1.2" fill="#6d737a"/><rect x="8" y="6" width="4" height="7" fill="#fff"/></svg>
          <span>11 97430-2816</span>
        </li>
        <li>
          <svg class="icon" viewBox="0 0 20 20"><circle cx="10" cy="10" r="9" fill="none" stroke="#6d737a" stroke-width="1.5"/><rect x="5" y="6.5" width="10" height="7" fill="none" stroke="#6d737a" stroke-width="1.3"/><path d="M5 6.5l5 4 5-4" fill="none" stroke="#6d737a" stroke-width="1.3"/></svg>
          <span>marina.castelo@verticeti.com.br</span>
        </li>
        <li>
          <svg class="icon" viewBox="0 0 20 20"><circle cx="10" cy="10" r="9" fill="none" stroke="#6d737a" stroke-width="1.5"/><circle cx="10" cy="10" r="5" fill="none" stroke="#6d737a" stroke-width="1.2"/><path d="M5 10h10M10 5c-2 3-2 7 0 10M10 5c2 3 2 7 0 10" fill="none" stroke="#6d737a" stroke-width="1"/></svg>
          <span>verticeti.com.br</span>
        </li>
      </ul>
    </div>
  </section>

  <section class="card card-back">
    <div class="back-top">
      <div class="section-head">
        <p class="kicker">Divisão de TI</p>
        <p class="title">Soluções em Tecnologia da Informação</p>
      </div>
      <ul class="service-list">
        <li>Administração e Suporte de TI (outsourcing)</li>
        <li>Cloud Solutions</li>
        <li>Locação e Venda de Hardware e Software</li>
        <li>Consultoria e Projetos de TI</li>
        <li>Segurança e Proteção de Dados</li>
      </ul>
    </div>
    <div class="back-bottom">
      <div class="section-head">
        <p class="kicker">Divisão de Eventos</p>
        <p class="title">Soluções para Gestão Jurídica</p>
      </div>
      <ul class="event-list">
        <li>Seminários</li>
        <li>Cursos</li>
        <li>Networking</li>
        <li>Congressos</li>
        <li>Workshop</li>
        <li>Conexões Empresariais</li>
        <li>Comitês</li>
      </ul>
    </div>
    <div class="back-edge"></div>
  </section>

</body>
</html>
```